Brovan Equipment Sales & Rentals

We are an independent equipment dealership located in the upstate of South Carolina. Our services include Equipment Sales, Equipment Rentals, Metal Sales, and Industrial Supplies.

I have attached our logos and a few billboards that we like as examples for inspiration. Thank you!

Phone Number 864-555-0172

Website link if you want to check out our page.
https://www.brovanmachinery.example

```html
<!DOCTYPE html>
<html lang="en">
<head>
<meta charset="utf-8">
<title>Brovan Equipment Sales &amp; Rentals – Billboard</title>
<link rel="stylesheet" href="https://fonts.googleapis.com/css2?family=Montserrat:wght@400;600;700;800;900&display=swap">
<style>
  :root {
    --red: #e31e26;
    --red-deep: #b0141b;
    --ink: #1c1c1c;
    --white: #ffffff;
    --board-bg: #f4f4f4;
    --page-bg: #e6e8eb;
    --machine-orange: #e9762a;
    --machine-yellow: #d9b93a;
  }
  * { box-sizing: border-box; margin: 0; padding: 0; }
  html, body { width: 1200px; height: 1200px; overflow: hidden; }
  body {
    background: var(--page-bg);
    font-family: "Montserrat", Arial, sans-serif;
    position: relative;
  }
  .billboard {
    position: absolute;
    left: 40px;
    top: 415px;
    width: 1120px;
    height: 370px;
    background: linear-gradient(180deg, var(--white) 0%, var(--board-bg) 60%, #e2e2e2 100%);
    overflow: hidden;
    box-shadow: 0 10px 30px rgba(0,0,0,0.18);
  }
  .billboard__shapes { position: absolute; inset: 0; }
  .services {
    position: absolute;
    left: 28px;
    top: 38px;
    color: var(--white);
    list-style: none;
    white-space: nowrap;
  }
  .services__item { margin-bottom: 24px; line-height: 1; }
  .services__label {
    display: block;
    font-weight: 400;
    font-size: 18px;
    letter-spacing: -0.3px;
  }
  .services__name {
    display: block;
    font-weight: 800;
    font-size: 28px;
    letter-spacing: -0.8px;
    margin-top: 2px;
  }
  .brand {
    position: absolute;
    left: 650px;
    top: 62px;
    display: flex;
    align-items: center;
    gap: 14px;
    white-space: nowrap;
  }
  .brand__mark {
    width: 38px;
    height: 38px;
    background: var(--red);
  }
  .brand__name {
    font-weight: 900;
    font-size: 76px;
    color: var(--ink);
    letter-spacing: -1.5px;
    line-height: 1;
  }
  .phone {
    position: absolute;
    left: 652px;
    top: 172px;
    display: flex;
    align-items: center;
    gap: 10px;
    white-space: nowrap;
  }
  .phone__icon { width: 32px; height: 32px; }
  .phone__number {
    font-weight: 700;
    font-size: 48px;
    color: var(--ink);
    letter-spacing: -0.5px;
    line-height: 1;
  }
  .website {
    position: absolute;
    right: 40px;
    top: 272px;
    font-weight: 600;
    font-size: 22px;
    color: var(--ink);
    line-height: 1;
    white-space: nowrap;
  }
</style>
</head>
<body>
  <section class="billboard" aria-label="Brovan Equipment Sales &amp; Rentals billboard">
    <svg class="billboard__shapes" width="1120" height="370" viewBox="0 0 1120 370">
      <defs>
        <linearGradient id="red-panel" x1="0" y1="0" x2="0" y2="1">
          <stop offset="0" stop-color="var(--red)"/>
          <stop offset="1" stop-color="var(--red-deep)"/>
        </linearGradient>
        <linearGradient id="machines" x1="0" y1="0" x2="1" y2="0">
          <stop offset="0" stop-color="var(--machine-yellow)" stop-opacity="0.85"/>
          <stop offset="0.45" stop-color="var(--machine-orange)" stop-opacity="0.9"/>
          <stop offset="1" stop-color="#8a5a3a" stop-opacity="0.9"/>
        </linearGradient>
        <linearGradient id="band" x1="0" y1="0" x2="1" y2="0">
          <stop offset="0" stop-color="var(--red)"/>
          <stop offset="1" stop-color="#ee2a30"/>
        </linearGradient>
      </defs>
      <polygon class="panel-red" points="0,0 330,0 412,370 0,370" fill="url(#red-panel)"/>
      <polygon class="panel-stripe" points="344,0 360,0 442,370 426,370" fill="var(--ink)"/>
      <rect class="photo-machines" x="215" y="22" width="410" height="330" rx="4" fill="url(#machines)"
            role="img" aria-label="Photo of a yellow and an orange tracked excavator with raised buckets"/>
      <polygon class="web-band" points="640,262 1120,250 1120,300 660,316" fill="url(#band)"/>
    </svg>

    <ul class="services">
      <li class="services__item"><span class="services__label">EQUIPMENT</span><span class="services__name">SALES</span></li>
      <li class="services__item"><span class="services__label">EQUIPMENT</span><span class="services__name">RENTALS</span></li>
      <li class="services__item"><span class="services__label">METAL</span><span class="services__name">SALES</span></li>
      <li class="services__item"><span class="services__label">INDUSTRIAL</span><span class="services__name">SUPPLIES</span></li>
    </ul>

    <div class="brand">
      <span class="brand__mark" aria-hidden="true"></span>
      <span class="brand__name">BROVAN</span>
    </div>

    <div class="phone">
      <svg class="phone__icon" viewBox="0 0 24 24" aria-hidden="true">
        <path d="M6.6 10.8a15.1 15.1 0 0 0 6.6 6.6l2.2-2.2a1 1 0 0 1 1-.25 11.4 11.4 0 0 0 3.6.57 1 1 0 0 1 1 1V20a1 1 0 0 1-1 1A17 17 0 0 1 3 4a1 1 0 0 1 1-1h3.5a1 1 0 0 1 1 1c0 1.250.2 2.45.57 3.57a1 1 0 0 1-.25 1z" fill="var(--red)"/>
      </svg>
      <span class="phone__number">864-555-0172</span>
    </div>

    <div class="website">www.brovanmachinery.example</div>
  </section>
</body>
</html>
```